TOBREL Business Card Design

We need a business card design for a current Plastering company now moving to building and constructing new homes.
We have been in the Plastering(rendering) business for 15yrs and have made a good name with our customers for our Top Quality of work that we provide.
We would like TOBREL to be the main attraction with an image of architectural roof tops or house design within it. Blue Yellow and Black are colours we like but are willing to see other ideas.
We would like the design to be modern and communicate quality and experience.
Industry/Entity Type
Building
Contact Information for Business Card
TOBREL Building and Plastering
PO BOX 73519 Casuarina Darwin NT 0812
PH/Fax: 08 83170925 Email: tobrel@wavemail.example
Glen: 0419372654 Ruth:0408631597
ABN:57 208 931 446

```html
<!DOCTYPE html>
<html lang="en">
<head>
<meta charset="utf-8">
<title>TOBREL Business Card</title>
<link href="https://fonts.googleapis.com/css2?family=Archivo:wdth,wght@62..125,600..800&display=swap" rel="stylesheet">
<style>
  :root {
    --backdrop: #e4e4e4;
    --card-white: #f4f4f2;
    --card-cream: #efede2;
    --brand-yellow: #edd100;
    --ink: #1c1c1c;
    --ink-soft: #2a2a2a;
    --name-grey: #a3a3a3;
    --sketch-light: #e2dfd2;
    --sketch-dark: #c9c6b8;
  }
  * { margin: 0; padding: 0; box-sizing: border-box; }
  html, body {
    width: 1200px;
    height: 720px;
    overflow: hidden;
    background: var(--backdrop);
    font-family: "Archivo", Arial, sans-serif;
    font-stretch: 90%;
  }
  .canvas {
    position: relative;
    width: 1200px;
    height: 720px;
  }
  .card {
    position: absolute;
    width: 420px;
    height: 220px;
    overflow: hidden;
    box-shadow: 0 2px 6px rgba(0,0,0,0.12);
  }

  /* Contact side */
  .card-contact {
    left: 390px;
    top: 110px;
    background: var(--card-white);
  }
  .card-contact .accent-panel {
    position: absolute;
    right: 0;
    top: 0;
    width: 155px;
    height: 100%;
    background: var(--brand-yellow);
  }
  .card-contact .brand-name {
    position: absolute;
    left: 40px;
    top: 36px;
    font-size: 36px;
    font-weight: 800;
    letter-spacing: 1px;
    color: var(--name-grey);
  }
  .contact-list {
    position: absolute;
    left: 46px;
    top: 100px;
    list-style: none;
    font-size: 10px;
    font-weight: 700;
    line-height: 12.5px;
    color: var(--ink-soft);
  }
  .postal {
    position: absolute;
    left: 54px;
    top: 160px;
    width: 205px;
    font-size: 10px;
    font-weight: 700;
    line-height: 12.5px;
    color: var(--ink-soft);
  }

  /* Brand side */
  .card-brand {
    left: 390px;
    top: 380px;
    background: var(--card-cream);
  }
  .card-brand .house-image {
    position: absolute;
    left: 28px;
    top: 12px;
    width: 300px;
    height: 208px;
    background: linear-gradient(160deg, var(--sketch-light) 0%, var(--sketch-dark) 55%, var(--sketch-light) 100%);
    opacity: 0.9;
  }
  .card-brand .side-band {
    position: absolute;
    left: 0;
    top: 0;
    width: 28px;
    height: 100%;
    background: var(--brand-yellow);
  }
  .card-brand .tag-band {
    position: absolute;
    left: 0;
    top: 130px;
    width: 100%;
    height: 28px;
    background: var(--brand-yellow);
  }
  .card-brand .brand-name {
    position: absolute;
    right: 34px;
    top: 28px;
    font-size: 38px;
    font-weight: 800;
    letter-spacing: 1px;
    color: var(--ink);
  }
  .card-brand .tagline {
    position: absolute;
    right: 16px;
    top: 135px;
    font-size: 14px;
    line-height: 18px;
    font-weight: 700;
    color: var(--ink);
  }
</style>
</head>
<body>
<main class="canvas">
  <section class="card card-contact" aria-label="Business card, contact side">
    <div class="accent-panel"></div>
    <h2 class="brand-name">TOBREL</h2>
    <ul class="contact-list">
      <li>Email: tobrel@wavemail.example</li>
      <li>Phone/Fax: 08 8317 0925</li>
      <li>Glen: 041 937 2654</li>
      <li>Ruth: 040 863 1597</li>
    </ul>
    <p class="postal">PO BOX 73519 , Fernhollow Ashport WT 0947<br>ABN: 57 208 931 446</p>
  </section>

  <section class="card card-brand" aria-label="Business card, brand side">
    <div class="house-image" role="img" aria-label="Faint line drawing of a modern two-storey house"></div>
    <div class="side-band"></div>
    <div class="tag-band"></div>
    <h1 class="brand-name">TOBREL</h1>
    <p class="tagline">Building and Plastering</p>
  </section>
</main>
</body>
</html>
```